Marta Business Card

My wife is going to start her own business with renting holiday appartments to tourists. She needs a design for a new business card... and a new web site.
Look at Stayvolt "Erholung auf dem Lindenwäldchen"

Target Market(s)

Give business card to prospects at any situation

Contact Information for Business Card

not sure what this means

Font styles to use
Script

Colors
fec41a
fee18a

Requirements
Must have
• My wife's handwriting is difficult to read:
Entspannen - Loslassen - Auftanken
Marta & das Lindenwäldchen
Urlaub an einem besonderen Ort
Marta Brecke
Grauer Pfad 7
18471 Alt Feldow
post@marta-brecke.de
www.lindenwaeldchen.net
Nice to have
• Beige background
Font like handwriting

```html
<!DOCTYPE html>
<html lang="de">
<head>
<meta charset="utf-8">
<title>Marta &amp; das Lindenwäldchen – Visitenkarte</title>
<link rel="stylesheet" href="https://fonts.googleapis.com/css2?family=Herr+Von+Muellerhoff&family=Kalam:wght@300;400&display=swap">
<style>
  :root {
    --backdrop: #5f5f5f;
    --card: #fdfbec;
    --ink: #141414;
    --sun: #f2d65c;
    --honey: #eac862;
    --amber: #e4bf66;
    --ochre: #dcb064;
    --script: "Herr Von Muellerhoff", cursive;
    --hand: "Kalam", cursive;
  }
  * { margin: 0; padding: 0; box-sizing: border-box; }
  html, body { width: 1200px; height: 800px; overflow: hidden; }
  body {
    background: var(--backdrop);
    position: relative;
    font-family: var(--hand);
    color: var(--ink);
  }
  .card {
    position: absolute;
    top: 232px;
    width: 520px;
    height: 336px;
    background: var(--card);
    overflow: hidden;
  }
  .card--front { left: 50px; }
  .card--back { left: 630px; }
  .card__bands {
    position: absolute;
    inset: 0;
    width: 100%;
    height: 100%;
  }
  .band--sun { fill: var(--sun); }
  .band--honey { fill: var(--honey); }
  .band--amber { fill: var(--amber); }
  .band--ochre { fill: var(--ochre); }

  /* front */
  .motto {
    position: absolute;
    font-family: var(--hand);
    font-weight: 300;
    font-size: 11px;
    letter-spacing: 0.3px;
  }
  .motto--relax { left: 36px; top: 28px; }
  .motto--release { left: 196px; top: 54px; }
  .motto--recharge { left: 436px; top: 20px; }
  .brand {
    position: absolute;
    left: 104px;
    top: 136px;
    width: 380px;
    text-align: center;
  }
  .brand__name {
    font-family: var(--script);
    font-weight: 400;
    font-size: 42px;
    line-height: 1.1;
    white-space: nowrap;
  }
  .brand__rule {
    height: 1px;
    background: var(--ink);
    margin: 2px 0 6px;
  }
  .brand__tagline {
    font-family: var(--hand);
    font-weight: 300;
    font-size: 12px;
    letter-spacing: 4px;
    white-space: nowrap;
  }

  /* back */
  .owner {
    position: absolute;
    left: 40px;
    top: 118px;
    width: 190px;
    font-family: var(--script);
    font-weight: 400;
    font-size: 42px;
    line-height: 1.1;
    white-space: nowrap;
  }
  .divider {
    position: absolute;
    left: 248px;
    top: 74px;
    width: 1px;
    height: 196px;
    background: var(--ink);
  }
  .contact {
    position: absolute;
    left: 268px;
    top: 124px;
    list-style: none;
  }
  .contact__item {
    display: flex;
    align-items: center;
    gap: 10px;
    font-family: var(--hand);
    font-size: 13px;
    height: 30px;
    white-space: nowrap;
  }
  .contact__icon { width: 12px; height: 12px; fill: var(--ink); flex: none; }
</style>
</head>
<body>

<section class="card card--front" aria-label="Vorderseite">
  <svg class="card__bands" viewBox="0 0 520 336" preserveAspectRatio="none" aria-hidden="true">
    <path class="band--sun" d="M0 0 H236 C214 30 205 70 196 110 C186 160 150 200 110 240 C80 270 62 300 46 336 H0 Z"/>
    <path class="band--honey" d="M0 0 H150 C132 50 120 100 96 150 C72 200 40 250 24 336 H0 Z"/>
    <path class="band--amber" d="M0 0 H78 C62 40 52 80 38 120 C24 160 10 200 0 240 Z"/>
    <path class="band--ochre" d="M0 0 H24 C16 18 8 34 0 52 Z"/>
  </svg>
  <span class="motto motto--relax">Entspannen</span>
  <span class="motto motto--release">Loslassen</span>
  <span class="motto motto--recharge">Auftanken</span>
  <div class="brand">
    <h1 class="brand__name">Marta &amp; das Lindenwäldchen</h1>
    <div class="brand__rule"></div>
    <p class="brand__tagline">Urlaub an einem besonderen Ort</p>
  </div>
</section>

<section class="card card--back" aria-label="Rückseite">
  <svg class="card__bands" viewBox="0 0 520 336" preserveAspectRatio="none" aria-hidden="true">
    <path class="band--sun" d="M450 0 H520 V336 H200 C240 320 280 300 310 270 C350 230 390 190 410 130 C425 80 440 40 450 0 Z"/>
    <path class="band--honey" d="M490 0 H520 V336 H250 C300 310 350 280 380 240 C420 190 450 130 470 70 Z"/>
    <path class="band--amber" d="M512 0 H520 V336 H330 C380 310 420 280 450 230 C480 180 500 100 512 0 Z"/>
    <path class="band--ochre" d="M520 260 V336 H470 C490 310 505 290 520 260 Z"/>
  </svg>
  <h2 class="owner">Marta Brecke</h2>
  <div class="divider"></div>
  <ul class="contact">
    <li class="contact__item">
      <svg class="contact__icon" viewBox="0 0 12 12" aria-hidden="true"><path d="M6 0a4 4 0 0 0-4 4c0 3 4 8 4 8s4-5 4-8a4 4 0 0 0-4-4zm0 5.5A1.5 1.5 0 1 1 6 2.5a1.5 1.5 0 0 1 0 3z"/></svg>
      <span>Grauer Pfad 7 , 18471 Alt Feldow</span>
    </li>
    <li class="contact__item">
      <svg class="contact__icon" viewBox="0 0 12 12" aria-hidden="true"><path d="M0 2h12v8H0z M1 3l5 4 5-4" stroke="#fdfbec" stroke-width="1"/></svg>
      <span>post@marta-brecke.de</span>
    </li>
    <li class="contact__item">
      <svg class="contact__icon" viewBox="0 0 12 12" aria-hidden="true"><circle cx="6" cy="6" r="6"/><path d="M0 6h12M6 0v12M6 0c-3 3-3 9 0 12M6 0c3 3 3 9 0 12" stroke="#fdfbec" stroke-width="0.8" fill="none"/></svg>
      <span>www.lindenwaeldchen.net</span>
    </li>
  </ul>
</section>

</body>
</html>
```